Mix one color into exisiting design, look premium

I have my existing designs, 7 packages. But I want to combine one color inside those designs. I want them to look fit perfectly and look expensive. Premium Products.

You may add anything or change design, make sure to mix the color.

Remember: Your task is to mix the color into my each one of the pakaging designs. Make into new design, look premium for baby products.

```html
<!DOCTYPE html>
<html lang="en">
<head>
<meta charset="UTF-8">
<title>Momo &amp; Pip Baby Diapers – Pack Front</title>
<link rel="stylesheet" href="https://fonts.googleapis.com/css2?family=Mali:wght@400;500;600&family=Kosugi+Maru&family=Fredoka:wght@600&display=swap">
<style>
  :root {
    --canvas-bg: #ffffff;
    --mint-top: #c9efe7;
    --mint-soft: #e6f7f3;
    --mint-wave: #b4e8dc;
    --teal-band: #4fcbae;
    --mint-mid: #a6e0d2;
    --blush: #f7d8de;
    --orange-light: #f7a640;
    --orange-deep: #ef8a22;
    --salmon: #f08d7a;
    --orange-type: #f0891f;
    --teal-type: #38bca4;
    --brand-red: #e2352f;
    --gold: #c9a45c;
    --gold-light: #e8d3a2;
    --icon-fill: rgba(255, 236, 205, 0.35);
    --label-brown: #9a5a26;
    --white: #ffffff;
  }
  * { margin: 0; padding: 0; box-sizing: border-box; }
  html, body { width: 900px; height: 1200px; overflow: hidden; background: var(--canvas-bg); }
  .canvas { position: relative; width: 900px; height: 1200px; }
  .pack-art { position: absolute; inset: 0; }

  .brand-name {
    position: absolute; left: 168px; width: 564px; top: 238px;
    text-align: center;
    font-family: "Fredoka", sans-serif; font-weight: 600; font-size: 34px;
    color: var(--brand-red); letter-spacing: 0.5px;
  }
  .brand-dot {
    display: inline-block; width: 14px; height: 14px; border-radius: 50%;
    background: var(--gold); margin-right: 10px; vertical-align: 4px;
  }
  .title-baby {
    position: absolute; left: 306px; top: 318px; height: 70px; width: 190px;
    font-family: "Mali", cursive; font-weight: 400; font-size: 54px; line-height: 70px;
    color: var(--salmon);
  }
  .title-baby span { position: absolute; top: 0; }
  .title-jp {
    position: absolute; left: 500px; top: 330px;
    font-family: "Kosugi Maru", sans-serif; font-size: 24px; line-height: 28px;
    color: var(--teal-type); white-space: nowrap;
  }
  .title-diapers {
    position: absolute; left: 302px; top: 370px;
    font-family: "Mali", cursive; font-weight: 500; font-size: 80px;
    color: var(--orange-type); letter-spacing: 0; line-height: 1.1;
  }
  .claim-pill {
    position: absolute; left: 308px; top: 478px; width: 298px; height: 31px;
    border-radius: 8px; background: var(--salmon);
    box-shadow: 0 0 0 1.5px var(--gold-light);
    font-family: "Mali", cursive; font-weight: 500; font-size: 17px;
    color: var(--white); letter-spacing: 1.5px;
    display: flex; align-items: center; justify-content: center;
  }
  .spec-labels {
    position: absolute; top: 941px; left: 0; width: 900px;
    font-family: "Mali", cursive; font-size: 13px; color: var(--label-brown);
  }
  .spec-labels span { position: absolute; width: 80px; margin-left: -40px; text-align: center; }
</style>
</head>
<body>
<main class="canvas">
  <svg class="pack-art" width="900" height="1200" viewBox="0 0 900 1200" xmlns="http://www.w3.org/2000/svg">
    <defs>
      <linearGradient id="skyGradient" x1="0" y1="0" x2="0" y2="1">
        <stop offset="0" stop-color="var(--mint-top)"/>
        <stop offset="0.6" stop-color="var(--mint-soft)"/>
      </linearGradient>
      <linearGradient id="orangeGradient" x1="0" y1="0" x2="0" y2="1">
        <stop offset="0" stop-color="var(--orange-light)"/>
        <stop offset="1" stop-color="var(--orange-deep)"/>
      </linearGradient>
      <clipPath id="packClip">
        <rect x="168" y="145" width="564" height="870" rx="6"/>
      </clipPath>
    </defs>

    <g class="pack" clip-path="url(#packClip)">
      <rect class="pack-sky" x="168" y="145" width="564" height="870" fill="url(#skyGradient)"/>
      <path class="wave-mint" fill="var(--mint-wave)"
            d="M168,578 C300,552 430,600 560,636 C640,658 700,652 732,642 L732,1015 L168,1015 Z"/>
      <path class="wave-teal" fill="var(--teal-band)"
            d="M168,690 C300,652 430,676 560,702 C650,718 700,706 732,694 L732,1015 L168,1015 Z"/>
      <path class="wave-mint-mid" fill="var(--mint-mid)"
            d="M168,706 C300,670 430,694 560,720 C650,736 700,724 732,712 L732,1015 L168,1015 Z"/>
      <path class="wave-blush" fill="var(--blush)"
            d="M168,752 C300,718 440,768 560,800 C650,824 700,820 732,812 L732,1015 L168,1015 Z"/>
      <path class="wave-gold-line" fill="none" stroke="var(--gold)" stroke-width="3"
            d="M168,770 C280,742 420,788 520,836 C620,882 690,864 732,850"/>
      <path class="wave-orange" fill="url(#orangeGradient)"
            d="M168,772 C280,744 420,790 520,838 C620,884 690,866 732,852 L732,1015 L168,1015 Z"/>

      <rect class="mascot-illustration" x="505" y="535" width="215" height="325" rx="40"
            fill="#f6c677" opacity="0.55" role="img"
            aria-label="Illustration of a smiling cartoon giraffe with floating hearts"/>

      <rect class="gold-frame" x="182" y="159" width="536" height="842" rx="4"
            fill="none" stroke="var(--gold)" stroke-width="1.5" opacity="0.85"/>
      <line class="gold-rule" x1="380" y1="296" x2="520" y2="296" stroke="var(--gold)" stroke-width="1.5"/>

      <g class="spec-icons" fill="var(--icon-fill)" stroke="var(--gold-light)" stroke-width="2">
        <circle cx="350" cy="908" r="25"/>
        <circle cx="422" cy="908" r="25"/>
        <circle cx="493" cy="908" r="25"/>
        <circle cx="563" cy="908" r="25"/>
      </g>
      <g class="spec-glyphs" fill="none" stroke="var(--gold-light)" stroke-width="2" stroke-linejoin="round">
        <path d="M337,898 H363 V905 C363,915 356,920 350,920 C344,920 337,915 337,905 Z"/>
        <circle cx="422" cy="912" r="8"/>
        <circle cx="422" cy="899" r="6"/>
        <rect x="487" y="893" width="12" height="12"/>
        <rect x="480" y="907" width="12" height="12"/>
        <rect x="494" y="907" width="12" height="12"/>
        <ellipse cx="563" cy="910" rx="9" ry="12"/>
        <circle cx="563" cy="903" r="5"/>
      </g>
    </g>
  </svg>

  <div class="brand-name"><span class="brand-dot"></span>Momo &amp; Pip</div>
  <div class="title-baby">
    <span style="left:2px">b</span>
    <span style="left:62px">a</span>
    <span style="left:122px">b</span>
    <span style="left:162px">y</span>
  </div>
  <div class="title-jp">のおむつ<br>赤ちゃん</div>
  <div class="title-diapers">diapers</div>
  <div class="claim-pill">360° HIP PROTECTION</div>

  <div class="spec-labels">
    <span style="left:350px">xxxl</span>
    <span style="left:422px">7–12kgs</span>
    <span style="left:493px">30pcs</span>
    <span style="left:563px">unisex</span>
  </div>
</main>
</body>
</html>
```